Music Industry Business Needs a Business Card Design

Copper Lantern is an audio mastering company that has been in business for 20 years. Mastering is the final creative step in the music production chain. Our job is to make the music sound as good as it possibly can prior to release to the public. Our world is technical, artistic, precise. We work on everything from independent artists to the music for the Grandfield Cup. We are looking for a new, more modern business card design. I am uploading a copy of our logo, although it doesn't absolutely need to be included in the design.

Target Market(s)

Music Industry Professionals

Industry/Entity Type

Business

Contact Information for Business Card

Address, Phone, Email, Website, Name, Job Title

Font styles to use
Sans Serif

Requirements
Must have
• Sorry, but I don't have any concrete things to request. If I had a clear idea of what I want, I would probably just design something myself. I am looking for fresh input and thought I would try this.
Should not have
• Anything that is typical, such as headphones or the like.

```html
<!DOCTYPE html>
<html lang="en">
<head>
<meta charset="utf-8">
<title>Copper Lantern – Business Card</title>
<link href="https://fonts.googleapis.com/css2?family=Open+Sans:wght@400;600&display=swap" rel="stylesheet">
<style>
  :root{
    --page:#e9e6e1;
    --card:#f4f4f4;
    --blue-deep:#1d4a92;
    --blue-main:#2659b0;
    --blue-light:#3b7ad8;
    --white:#ffffff;
    --ink:#1c1c1c;
    --pill:rgba(255,255,255,0.12);
  }
  html,body{margin:0;padding:0;width:1200px;height:1023px;overflow:hidden;background:var(--page);}
  body{position:relative;font-family:"Open Sans",Arial,sans-serif;}
  .card{position:absolute;top:160px;width:400px;height:700px;border-radius:22px;overflow:hidden;background:var(--card);box-shadow:0 14px 34px rgba(0,0,0,0.18);}
  .card--front{left:170px;}
  .card--back{left:630px;}
  .card svg.card-art{position:absolute;inset:0;width:400px;height:700px;}
  .brand{position:absolute;display:flex;align-items:center;gap:10px;color:var(--ink);font-weight:400;font-size:21px;letter-spacing:1px;text-transform:uppercase;}
  .brand__dot{width:12px;height:12px;border-radius:50%;background:var(--blue-main);}
  .card--front .brand{top:44px;right:34px;}
  .card--back .brand{bottom:90px;left:0;right:0;justify-content:center;font-size:24px;}
  .holder{position:absolute;left:48px;top:190px;color:var(--white);}
  .holder__name{font-size:30px;font-weight:400;margin:0;line-height:1.1;}
  .holder__role{font-size:16px;margin:4px 0 0;opacity:.9;}
  .contacts{position:absolute;left:30px;top:292px;margin:0;padding:0;list-style:none;}
  .contacts li{display:flex;align-items:center;gap:14px;height:32px;margin-bottom:12px;padding:0 16px 0 10px;background:var(--pill);border-radius:0 16px 16px 0;color:var(--white);font-size:17px;}
  .contacts svg{width:20px;height:20px;flex:none;fill:var(--white);}
</style>
</head>
<body>

<section class="card card--front" aria-label="Card front">
  <svg class="card-art" viewBox="0 0 400 700">
    <path d="M0,70 C120,40 150,230 400,180 L400,700 L330,700 C280,610 160,590 0,610 Z" fill="var(--blue-light)"/>
    <path d="M0,95 C120,70 160,245 400,205 L400,700 L310,700 C260,625 150,600 0,590 Z" fill="var(--blue-main)"/>
    <path d="M0,130 C110,110 170,260 400,232 L400,700 L295,700 C250,640 150,610 0,570 Z" fill="var(--blue-deep)" opacity=".85"/>
    <path d="M0,570 C150,610 250,640 295,700 L400,700 L400,560 C300,620 150,560 0,480 Z" fill="var(--blue-light)" opacity=".35"/>
  </svg>
  <div class="brand"><span class="brand__dot"></span>Copper Lantern</div>
  <div class="holder">
    <p class="holder__name">Marcus Hale</p>
    <p class="holder__role">Director</p>
  </div>
  <ul class="contacts">
    <li><svg viewBox="0 0 24 24"><path d="M6.6 10.8a15 15 0 0 0 6.6 6.6l2.2-2.2c.3-.3.7-.4 1-.2 1.1.4 2.3.6 3.6.6.6 0 1 .4 1 1V20c0 .6-.4 1-1 1C10.6 21 3 13.4 3 4c0-.6.4-1 1-1h3.5c.6 0 1 .4 1 1 0 1.3.2 2.5.6 3.6.1.3 0 .7-.2 1z"/></svg>5550 182 406</li>
    <li><svg viewBox="0 0 24 24"><path d="M8 2h8a2 2 0 0 1 2 2v16a2 2 0 0 1-2 2H8a2 2 0 0 1-2-2V4a2 2 0 0 1 2-2zm0 3v13h8V5zm4 14.2a1 1 0 1 0 0 2 1 1 0 0 0 0-2z"/></svg>5550 182 406</li>
    <li><svg viewBox="0 0 24 24"><path d="M3 5h18v14H3zm2 2v.4l7 5 7-5V7zm0 2.8V17h14V9.8l-7 5z"/></svg>copperlantern</li>
    <li><svg viewBox="0 0 24 24"><path d="M12 2a10 10 0 1 0 0 20 10 10 0 0 0 0-20zm6.9 9h-3a15 15 0 0 0-1.3-5.5A8 8 0 0 1 18.9 11zM12 4.1c.9 1.3 1.8 3.8 1.9 6.9h-3.8c.1-3.1 1-5.6 1.9-6.9zM9.4 5.5A15 15 0 0 0 8.1 11h-3a8 8 0 0 1 4.3-5.5zM5.1 13h3a15 15 0 0 0 1.3 5.5A8 8 0 0 1 5.1 13zm6.9 6.9c-.9-1.3-1.8-3.8-1.9-6.9h3.8c-.1 3.1-1 5.6-1.9 6.9zm2.6-1.4a15 15 0 0 0 1.3-5.5h3a8 8 0 0 1-4.3 5.5z"/></svg>www.copperlantern.com</li>
    <li><svg viewBox="0 0 24 24"><path d="M12 2a7 7 0 0 0-7 7c0 5.2 7 13 7 13s7-7.8 7-13a7 7 0 0 0-7-7zm0 9.5A2.5 2.5 0 1 1 12 6.5a2.5 2.5 0 0 1 0 5z"/></svg>48 Harbor Lane, Brookfield</li>
  </ul>
</section>

<section class="card card--back" aria-label="Card back">
  <svg class="card-art" viewBox="0 0 400 700">
    <path d="M0,0 L400,0 L400,250 C260,240 180,440 0,470 Z" fill="var(--blue-light)"/>
    <path d="M0,0 L400,0 L400,220 C250,215 170,410 0,440 Z" fill="var(--blue-main)"/>
    <path d="M0,0 L400,0 L400,190 C240,190 160,380 0,405 Z" fill="var(--blue-deep)" opacity=".85"/>
  </svg>
  <div class="brand"><span class="brand__dot"></span>Copper Lantern</div>
</section>

</body>
</html>
```